Tindale Cosmetic Clinic

I would like a youthful fresh design that appeals to women 25-75 age bracket...Colours purples/pinks/splash orange something like:

Refresh, renew ,revitalize!

Book in for a consult! Only $80
An experienced, specialist cosmetic physician will give you a personalized insight into your treatment requirements using antiwrinkle injections and fillers
Your consultation fee will be refunded if you opt to go ahead with treatment.

www.tindalecosmetic-demo.com
located Within Tindale Medical Clinic, 7C pellam st, ferrow 5209
phone 0491 637584 and speak to Rhona

Drs Marguerite Volk ,Tarek Qudsi and Yvonne Pettigrew

```html
<!DOCTYPE html>
<html lang="en">
<head>
<meta charset="utf-8">
<title>Tindale Cosmetic Clinic – Consult Flyer</title>
<link rel="stylesheet" href="https://fonts.googleapis.com/css2?family=Ubuntu:ital,wght@0,400;0,500;1,400;1,500&display=swap">
<style>
  :root {
    --page-bg: #ecebe8;
    --paper: #ffffff;
    --lavender: #8a84bf;
    --title-purple: #7d6cb2;
    --pink: #e2147f;
    --ink: #3f3f3f;
    --body-ink: #575757;
    --band: #231f20;
    --band-text: #ffffff;
    --skin-light: #f6e6dc;
    --skin-mid: #e9cdbd;
    --towel: #d9c9b6;
  }
  * { margin: 0; padding: 0; box-sizing: border-box; }
  html, body {
    width: 1200px; height: 937px; overflow: hidden;
    background: var(--page-bg);
    font-family: "Ubuntu", sans-serif;
  }
  .flyer {
    position: absolute; left: 48px; top: 42px;
    width: 1104px; height: 851px;
    background: var(--paper);
    overflow: hidden;
    box-shadow: 0 2px 6px rgba(0,0,0,.18);
  }
  .hero-photo {
    position: absolute; left: 0; top: 0; width: 580px; height: 851px;
    background:
      radial-gradient(ellipse 150px 120px at 300px 120px, var(--towel) 0%, rgba(217,201,182,0) 100%),
      radial-gradient(ellipse 260px 360px at 290px 420px, var(--skin-mid) 0%, var(--skin-light) 55%, rgba(255,255,255,0) 100%),
      linear-gradient(90deg, rgba(255,255,255,0) 70%, var(--paper) 100%);
  }
  .corner-swoosh { position: absolute; left: 0; top: 570px; width: 580px; height: 281px; }
  .site-link {
    position: absolute; left: 28px; top: 808px;
    display: flex; align-items: center; gap: 10px;
    color: var(--paper); font-size: 21px;
  }
  .site-link svg { width: 18px; height: 18px; }
  .info { position: absolute; left: 530px; top: 0; width: 574px; }
  .clinic-name {
    position: absolute; top: 78px; left: 0;
    font-size: 43px; font-weight: 500; color: var(--title-purple);
    white-space: nowrap;
  }
  .phone-line {
    position: absolute; top: 160px; left: 0;
    font-size: 24px; font-weight: 500; color: var(--ink);
  }
  .headline {
    position: absolute; top: 209px; left: 0;
    font-size: 36px; font-weight: 500; color: var(--pink);
  }
  .intro {
    position: absolute; top: 271px; left: 0; width: 520px;
    font-size: 20px; line-height: 32px; color: var(--body-ink);
  }
  .refund-band {
    position: absolute; top: 420px; left: -1px; width: 576px; height: 100px;
    background: var(--band); color: var(--band-text);
    font-size: 24px; font-style: italic; font-weight: 500; line-height: 38px;
    padding: 11px 0 0 20px;
  }
  .offer {
    position: absolute; top: 537px; left: 0;
    font-size: 34px; font-weight: 500; color: var(--pink);
  }
  .location {
    position: absolute; top: 606px; left: 0;
    font-size: 25px; font-weight: 500; color: var(--ink);
  }
  .doctors {
    position: absolute; top: 650px; left: 0;
    font-size: 23px; line-height: 36px; color: var(--body-ink);
  }
  .contact {
    position: absolute; left: 0; display: flex; align-items: center; gap: 8px;
    font-size: 25px; color: var(--ink);
  }
  .contact svg { flex: none; }
  .contact--address { top: 743px; }
  .contact--email { top: 795px; }
</style>
</head>
<body>
  <main class="flyer">
    <div class="hero-photo" role="img" aria-label="Photo of a smiling woman with a towel wrapped on her head, hands resting against her cheek"></div>

    <svg class="corner-swoosh" viewBox="0 0 580 281" preserveAspectRatio="none" aria-hidden="true">
      <path d="M0 0 C120 170 330 255 580 281 L0 281 Z" fill="var(--lavender)"/>
    </svg>

    <div class="site-link">
      <svg viewBox="0 0 20 20" aria-hidden="true">
        <circle cx="10" cy="10" r="9" fill="var(--pink)"/>
        <g fill="none" stroke="#fff" stroke-width="1.2">
          <ellipse cx="10" cy="10" rx="4" ry="8.5"/>
          <line x1="1.5" y1="10" x2="18.5" y2="10"/>
          <line x1="3" y1="5.5" x2="17" y2="5.5"/>
          <line x1="3" y1="14.5" x2="17" y2="14.5"/>
        </g>
      </svg>
      <span>www.tindalecosmetic-demo.com</span>
    </div>

    <section class="info">
      <h1 class="clinic-name">Tindale Cosmetic Clinic</h1>
      <p class="phone-line">Phone 0491 637584 and speak to Rhona</p>
      <h2 class="headline">Refresh, Renew, Revitalize!</h2>
      <p class="intro">An experienced, specialist cosmetic physician will give you a personalized insight into your treatment requirements using anti-wrinkle injections<br>and fillers</p>
      <p class="refund-band">Your consultation fee will be refunded if you<br>opt to go ahead with treatment.</p>
      <p class="offer">Book in for a consult! Only $80</p>
      <p class="location">Located Within Tindale Medical Clinic</p>
      <p class="doctors">Drs Marguerite Volk ,Tarek Qudsi and<br>Yvonne Pettigrew</p>
      <p class="contact contact--address">
        <svg width="22" height="28" viewBox="0 0 22 28" aria-hidden="true">
          <path d="M11 1C5.5 1 2 5 2 10c0 6.5 9 17 9 17s9-10.5 9-17c0-5-3.5-9-9-9z" fill="var(--pink)"/>
          <circle cx="11" cy="10" r="3.6" fill="#fff"/>
        </svg>
        <span>7C pellam st, ferrow 5209</span>
      </p>
      <p class="contact contact--email">
        <svg width="24" height="18" viewBox="0 0 24 18" aria-hidden="true">
          <rect x="1" y="2" width="22" height="14" fill="none" stroke="var(--pink)" stroke-width="2"/>
          <path d="M1 2 L12 11 L23 2" fill="none" stroke="var(--pink)" stroke-width="2"/>
        </svg>
        <span>info@tindalecosmetic-demo.com</span>
      </p>
    </section>
  </main>
</body>
</html>
```